Sprout & Soar General Card Design

Please see http://sprout-and-soar.example.org for more information about our program. In brief, we are a 501(c)(3) nonprofit organization that focuses on improving educational outcomes for all students through parent education and empowerment, K-12 curriculum development, K-12 staff development, learner-oriented live events, community service projects, and more. We are now preparing to launch our Sprout & Soar Educational Series, which is devoted to teaching children and the adults in their lives about making healthy food choices and regaining control over what is in their food by growing it themselves in easy, affordable self-watering container gardens that can be placed in spaces not otherwise suitable for growing fruits and vegetables, such as paved lots and rooftops, are portable, and can be quickly built from recycled materials. In fact, we have local businesses already lining up to donate clean, safe 5-gallon buckets for this initiative (our container design uses 5-gallon buckets). We have already built out content on the site to support as many of the Trail Rover merit badges as we could tie to the instructional goals of our Sprout & Soar Educational Series. We are in the processes of developing K-12 curricula tied to the Common Core and STEM (science, technology, engineering, & math), which we will be giving away for free under a Creative Commons license to help public schools in states that have recently adopted the Common Core but can't afford to replace all their textbooks and don't have the time to scramble to create curricula of their own. This card will be used by all of our Sprout & Soar staff and volunteers to share out information about the program and promote it to others. It will go out in mailings, sit on display tables at events, be left at kiosks, and be handed out in person. It needs to be color-matched to our Sprout & Soar site. The logo on the site we created for our Sprout & Soar Educational Series was done using an online service and the quality of the image is quite poor (see attached file). When we use it in print materials and then convert them to PDF, the logo becomes pixelated. It's awful. We are not entirely married to keeping the logo if you can come up with something better and we are given the final JPG or PNG file of the logo to upload to the site so they match. If you can just improve the quality of the existing logo, that's fine, too. Please note that the phrase "Sprout & Soar Educational Series" is a service mark of BrightHome4Kids and should be followed by the letters "SM" in superscript at the end of the word "Series" in any logo you create.
Target Market(s)
parents of K-12 students, K-12 teachers, community service organizations, youth organizations, programs for the elderly, programs for the disabled
Industry/Entity Type
Community Service
Contact Information for Business Card
BrightHome4Kids' Sprout & Soar Educational Series, http://sprout-and-soar.example.org, (555) 214-7389, Non-GMO/Organic Family & Community Gardening Workshops, K-12 Common Core/STEM Curricula Development, Community Service Projects, Online Gardening & Teaching Communities, Project-Based Learning Activities, Youth Leadership Projects, Fun Contests and Prizes, Corporate & Small Business Social Responsibility Programs, K-12 Staff Development, Education Research & Reporting

```html
<!DOCTYPE html>
<html lang="en">
<head>
<meta charset="utf-8">
<title>Sprout &amp; Soar Educational Series – Card Options</title>
<link href="https://fonts.googleapis.com/css2?family=Crimson+Text:wght@600;700&family=Questrial&family=Arimo:wght@700&display=swap" rel="stylesheet">
<style>
  :root {
    --page: #ffffff;
    --frame: #e4e4e4;
    --green-light: #eef7d6;
    --green-mid: #a6d46a;
    --green-deep: #5fae2c;
    --title: #3f7a1e;
    --ink-dark: #1f2a12;
    --ink-list: #2c3a1c;
    --bullet: #f3a21b;
    --swoosh-orange: #f0901c;
    --swoosh-white: #ffffff;
  }
  * { box-sizing: border-box; margin: 0; padding: 0; }
  html, body { width: 788px; height: 1200px; overflow: hidden; }
  body {
    position: relative;
    background: var(--page);
    font-family: "Questrial", sans-serif;
  }
  .sheet-frame {
    position: absolute; inset: 0;
    border: 1px solid var(--frame);
  }
  .option-number {
    position: absolute; left: 22px;
    font-family: "Arimo", sans-serif; font-weight: 400;
    font-size: 26px; color: #222;
  }
  .card {
    position: absolute;
    width: 300px; height: 512px;
    overflow: hidden;
    background: radial-gradient(ellipse 75% 55% at 50% 45%, var(--green-light) 0%, var(--green-mid) 60%, var(--green-deep) 100%);
    box-shadow: 2px 3px 6px rgba(0,0,0,0.28);
  }
  .photo { position: absolute; left: 0; display: block; }
  .series-title {
    position: absolute; left: 0; width: 100%;
    text-align: center;
    font-family: "Crimson Text", serif; font-weight: 700;
    color: var(--title);
    line-height: 1;
  }
  .series-title .name { display: block; font-size: 35px; }
  .series-title .series { display: block; font-size: 26px; margin-top: 3px; }
  .series-title sup { font-size: 8px; vertical-align: 14px; font-family: "Arimo", sans-serif; }
  .contact {
    position: absolute; left: 0; width: 100%;
    text-align: center;
    font-family: "Arimo", sans-serif; font-weight: 700;
    font-size: 14.5px; color: var(--ink-dark);
  }
  .contact .phone { display: block; margin-top: 13px; }
  .contact svg { width: 13px; height: 15px; vertical-align: -2px; margin-right: 2px; }
  .partner-name {
    position: absolute; left: 10px; bottom: 10px;
    display: flex; align-items: center; gap: 5px;
    font-family: "Arimo", sans-serif; font-weight: 700;
    font-size: 13px; color: #ffffff;
  }
  .partner-name .dot { width: 12px; height: 12px; border-radius: 50%; background: #ffffff; }
  .services {
    position: absolute; left: 28px; right: 8px;
    list-style: none;
    font-size: 12.6px; line-height: 16.8px;
    color: var(--ink-list);
  }
  .services li { position: relative; padding-left: 11px; }
  .services li::before {
    content: ""; position: absolute; left: 0; top: 5px;
    width: 6px; height: 6px; border-radius: 50%;
    background: var(--bullet);
    box-shadow: 0 0 0 1px #fbd27a;
  }
</style>
</head>
<body>
<div class="sheet-frame"></div>

<!-- Option 1 -->
<div class="option-number" style="top:52px;">1</div>

<section class="card card-front" style="left:58px; top:48px;">
  <svg class="photo" style="top:0;" width="300" height="170" viewBox="0 0 300 170" role="img" aria-label="Photo of purple and orange pansies in a red garden pot">
    <defs>
      <linearGradient id="pansyTones" x1="0" y1="0" x2="1" y2="1">
        <stop offset="0" stop-color="#5b3f7a"/>
        <stop offset="0.45" stop-color="#4d6b2e"/>
        <stop offset="0.8" stop-color="#b8483a"/>
        <stop offset="1" stop-color="#8a2f2a"/>
      </linearGradient>
    </defs>
    <path d="M0,0 H300 V112 Q170,168 0,140 Z" fill="url(#pansyTones)"/>
    <path d="M0,142 Q170,170 300,114" fill="none" stroke="var(--swoosh-white)" stroke-width="5"/>
    <path d="M0,150 Q170,176 300,122" fill="none" stroke="var(--swoosh-orange)" stroke-width="3"/>
  </svg>

  <h1 class="series-title" style="top:163px;">
    <span class="name">Sprout &amp; Soar</span>
    <span class="series">Educational Series<sup>SM</sup></span>
  </h1>

  <p class="contact" style="top:250px;">
    sprout-and-soar.example.org
    <span class="phone"><svg viewBox="0 0 24 28"><path d="M6 2 L10 2 L12 9 L9 11 Q11 17 15 20 L18 17 L23 20 L22 25 Q20 27 16 26 Q5 21 3 8 Q3 3 6 2 Z" fill="var(--ink-dark)"/></svg>(555) 214-7389</span>
  </p>

  <svg class="photo" style="top:300px;" width="300" height="212" viewBox="0 0 300 212" role="img" aria-label="Photo of cucumber seedlings growing in red buckets">
    <defs>
      <linearGradient id="bucketTones" x1="0" y1="0" x2="0" y2="1">
        <stop offset="0" stop-color="#4f7d30"/>
        <stop offset="0.5" stop-color="#3a3a2a"/>
        <stop offset="1" stop-color="#a8302a"/>
      </linearGradient>
    </defs>
    <path d="M0,38 Q130,-6 300,14 V212 H0 Z" fill="url(#bucketTones)"/>
    <path d="M0,36 Q130,-8 300,12" fill="none" stroke="var(--swoosh-white)" stroke-width="4"/>
    <path d="M0,30 Q130,-14 300,6" fill="none" stroke="var(--swoosh-orange)" stroke-width="3"/>
  </svg>

  <div class="partner-name"><span class="dot"></span>BrightHome4Kids</div>
</section>

<section class="card card-back" style="left:428px; top:46px;">
  <h2 class="series-title" style="top:20px;">
    <span class="name">Sprout &amp; Soar</span>
    <span class="series">Educational Series<sup>SM</sup></span>
  </h2>
  <ul class="services" style="top:100px;">
    <li>Non-GMO/Organic Family &amp; Community<br>Gardening Workshops;</li>
    <li>K-12 Common Core/STEM Curricula<br>Development;</li>
    <li>Community Service Projects;</li>
    <li>Online Gardening &amp; Teaching<br>Communities;</li>
    <li>Project-Based Learning Activities;</li>
    <li>Youth Leadership Projects;</li>
    <li>Fun Contests and Prizes;</li>
    <li>Corporate &amp; Small Business Social<br>Responsibility Programs;</li>
    <li>K-12 Staff Development<br>Education Research &amp; Reporting.</li>
  </ul>
  <svg class="photo" style="top:344px;" width="300" height="168" viewBox="0 0 300 168" role="img" aria-label="Photo of many cupped hands holding small green seedlings in soil">
    <defs>
      <linearGradient id="handsTones" x1="0" y1="0" x2="1" y2="1">
        <stop offset="0" stop-color="#2f5a22"/>
        <stop offset="0.5" stop-color="#b98a66"/>
        <stop offset="1" stop-color="#4a3a28"/>
      </linearGradient>
    </defs>
    <path d="M0,40 Q140,-10 300,26 V168 H0 Z" fill="url(#handsTones)"/>
    <path d="M0,38 Q140,-12 300,24" fill="none" stroke="var(--swoosh-white)" stroke-width="4"/>
    <path d="M0,32 Q140,-18 300,18" fill="none" stroke="var(--swoosh-orange)" stroke-width="3"/>
  </svg>
</section>

<!-- Option 2 -->
<div class="option-number" style="top:625px;">2</div>

<section class="card card-front" style="left:60px; top:622px;">
  <svg class="photo" style="top:0;" width="300" height="340" viewBox="0 0 300 340" role="img" aria-label="Photo of a young child smiling at a pepper seedling in a pot of soil">
    <defs>
      <linearGradient id="childTones" x1="0" y1="0" x2="0" y2="1">
        <stop offset="0" stop-color="#d9b394"/>
        <stop offset="0.45" stop-color="#e9ddd0"/>
        <stop offset="0.75" stop-color="#3a2a1e"/>
        <stop offset="1" stop-color="#c8321f"/>
      </linearGradient>
    </defs>
    <path d="M0,0 H300 V316 Q150,340 0,316 Z" fill="url(#childTones)"/>
    <path d="M0,318 Q150,342 300,318" fill="none" stroke="var(--swoosh-orange)" stroke-width="3"/>
  </svg>

  <h1 class="series-title" style="top:356px;">
    <span class="name">Sprout &amp; Soar</span>
    <span class="series">Educational Series<sup>SM</sup></span>
  </h1>

  <p class="contact" style="top:443px;">
    sprout-and-soar.example.org
    <span class="phone"><svg viewBox="0 0 24 28"><path d="M6 2 L10 2 L12 9 L9 11 Q11 17 15 20 L18 17 L23 20 L22 25 Q20 27 16 26 Q5 21 3 8 Q3 3 6 2 Z" fill="var(--ink-dark)"/></svg>(555) 214-7389</span>
  </p>
</section>

<section class="card card-back" style="left:427px; top:618px;">
  <h2 class="series-title" style="top:22px;">
    <span class="name">Sprout &amp; Soar</span>
    <span class="series">Educational Series<sup>SM</sup></span>
  </h2>
  <ul class="services" style="top:100px;">
    <li>Non-GMO/Organic Family &amp; Community<br>Gardening Workshops;</li>
    <li>K-12 Common Core/STEM Curricula<br>Development;</li>
    <li>Community Service Projects;</li>
    <li>Online Gardening &amp; Teaching<br>Communities;</li>
    <li>Project-Based Learning Activities;</li>
    <li>Youth Leadership Projects;</li>
    <li>Fun Contests and Prizes;</li>
    <li>Corporate &amp; Small Business Social<br>Responsibility Programs;</li>
    <li>K-12 Staff Development<br>Education Research &amp; Reporting.</li>
  </ul>
  <svg class="photo" style="top:340px;" width="300" height="176" viewBox="0 0 300 176" role="img" aria-label="Photo of cucumber seedlings growing in red buckets">
    <defs>
      <linearGradient id="bucketTones2" x1="0" y1="0" x2="0" y2="1">
        <stop offset="0" stop-color="#4f7d30"/>
        <stop offset="0.55" stop-color="#3a3a2a"/>
        <stop offset="1" stop-color="#a8302a"/>
      </linearGradient>
    </defs>
    <path d="M0,46 Q150,-18 300,46 V176 H0 Z" fill="url(#bucketTones2)"/>
    <path d="M0,44 Q150,-20 300,44" fill="none" stroke="var(--swoosh-white)" stroke-width="4"/>
    <path d="M0,38 Q150,-26 300,38" fill="none" stroke="var(--swoosh-orange)" stroke-width="4"/>
  </svg>
</section>
</body>
</html>
```